Investment Company Business Card Design

We need a Business Card design for a new company based in Boston called "Olt Investment". We are cooperating with local real estate and construction companies. Our company is very actively and aggressively acquiring primarily residential investment properties either to buy and hold long term or for purposes or renovating and repositioning for re-sale in the market. In addition, we undertake some development projects and acquisitions as opportunities present themselves. the final design should contains information about “Olt" the river boat. we are tenacious, indomitable, and the business have a favorable wind throughout the voyage for all our investment.
sample Info. on Design:
Tem Hollis
CEO
508-xxx-xxxx
415 Marrow St. Suite 108, Boston, MA 02127
Please provide a template also, that we can edit the info later.
Reason: i just got new LOGO Design attached will be use in Business Card Design.
Construction

```html
<!DOCTYPE html>
<html lang="en">
<head>
<meta charset="utf-8">
<title>Olt Investment – Business Card</title>
<link href="https://fonts.googleapis.com/css2?family=Open+Sans:wght@400;600;700&display=swap" rel="stylesheet">
<style>
  :root {
    --page: #e9e7e1;
    --white: #fbfbfb;
    --band-light: #c9c9cb;
    --band-dark: #a9a9ab;
    --panel-grey: #bdbdbf;
    --gold: #b8954a;
    --ink: #111111;
    --ink-soft: #3a3a3a;
    --muted: #555555;
  }
  * { box-sizing: border-box; margin: 0; padding: 0; }
  html, body { width: 1200px; height: 800px; overflow: hidden; }
  body {
    background: var(--page);
    font-family: "Open Sans", Arial, sans-serif;
    display: flex;
    align-items: center;
    justify-content: center;
    gap: 48px;
  }
  .card {
    position: relative;
    width: 540px;
    height: 309px;
    overflow: hidden;
    box-shadow: 0 6px 18px rgba(0,0,0,0.18);
  }

  /* Back of card */
  .card-back {
    background: linear-gradient(180deg,
      var(--band-light) 0%, var(--band-light) 30%,
      var(--white) 30%, #ececec 68%,
      var(--band-dark) 68%, var(--band-dark) 100%);
  }
  .card-back .brand {
    position: absolute;
    left: 0; right: 0;
    top: 30%; height: 38%;
    display: flex; align-items: center; justify-content: center;
  }

  .brand-name {
    color: var(--gold);
    font-weight: 600;
    letter-spacing: 0.04em;
    text-transform: uppercase;
    white-space: nowrap;
  }
  .card-back .brand-name { font-size: 34px; }

  /* Front of card */
  .card-front { background: var(--white); }
  .card-front .curve { position: absolute; inset: 0; }
  .card-front .brand {
    position: absolute;
    left: 0; top: 0;
    width: 240px; height: 100%;
    display: flex; align-items: center; justify-content: center;
  }
  .card-front .brand-name { font-size: 24px; }

  .contact {
    position: absolute;
    right: 26px;
    text-align: right;
  }
  .contact-name {
    top: 40px;
    font-size: 26px;
    font-weight: 700;
    color: var(--ink);
    line-height: 1;
  }
  .contact-role {
    display: block;
    font-size: 11px;
    font-weight: 400;
    color: var(--muted);
    margin-top: 2px;
  }
  .contact-phone {
    top: 152px;
    font-size: 17px;
    color: var(--ink-soft);
  }
  .contact-address {
    top: 258px;
    font-size: 13px;
    color: var(--muted);
  }
</style>
</head>
<body>

  <section class="card card-back" aria-label="Business card back">
    <div class="brand"><span class="brand-name">Olt Invest</span></div>
  </section>

  <section class="card card-front" aria-label="Business card front">
    <svg class="curve" viewBox="0 0 540 309" width="540" height="309" aria-hidden="true">
      <path d="M195 0 Q300 110 305 309 L540 309 L540 0 Z" fill="var(--panel-grey)"/>
      <path d="M195 0 Q300 110 305 309" fill="none" stroke="var(--gold)" stroke-width="1.5"/>
    </svg>
    <div class="brand"><span class="brand-name">Olt Invest</span></div>
    <p class="contact contact-name">Tem Hollis<span class="contact-role">CEO</span></p>
    <p class="contact contact-phone">Phone: 508-xxx-xxxx</p>
    <p class="contact contact-address">415 Marrow St. Suite 108, Boston, MA 02127</p>
  </section>

</body>
</html>
```